4 x 9 Rack Card Design: Cheer Each Game Advertising Campaign

We would like a 4 x 9 Rack Card Designed using our logo as the basis for the design. We would like to incorporate the images of the shoes & the colors that are on our logo. We are attaching an image of the logo for your use.

The design should use both the front & back of the 4 x 9 card.

All text & fonts should be in "comic sans".

The card should have a fun, youthful, cartoon feel to it.

We would like the following information on the card:

Our Tag Line: Charity providing Athletic Footwear to Kids

Our Catch Phrase: "Cheer Each Game". Please include small images of various sports balls under, or around or near the catch phrase. Please use images of a Basketball, baseball, golf ball, soccer ball, Hockey Puck, American Football, Tennis ball.

Our Contact Information: PO Box 57392, Phoenix, AZ 85077; phone 480.312.4456; www.hop-and-laces.org; also use the "find us on chatterbook" image.

Who we are: We are a 501(c)3 non-profit organization providing athletic footwear to disadvantaged and at-risk youth. The proper footwear allows participation in sports activities providing a healthy outlet for energy, increased self confidence, reduced juvenile crime rates, decline in alcohol, tobacco and drug dependency, strengthened relationships and enhanced academic performance.

A Recipe: We are working on a recipe to be included. In the meantime, we are asking for designs that include a small area for a recipe on the back of the card. The recipe will be easy, with very few ingredients & instructions, so it won't take up too much space on the rack card.

Target Market(s)

Sponsors, endorsers, donators, sports teams.

Industry/Entity Type

Non-Profit

Font styles to use
Other font styles liked:
• Comic Sans

Requirements
Must have
• See project descripion
Nice to have
• See project description. Also, please take a look at our website at www.hop-and-laces.com for our style & additional information about our organization.

```html
<!DOCTYPE html>
<html lang="en">
<head>
<meta charset="utf-8">
<title>Hop-and-Laces Rack Card</title>
<link rel="stylesheet" href="https://fonts.googleapis.com/css2?family=Comic+Neue:wght@400;700&display=swap">
<style>
  :root {
    --green: #86b162;
    --green-light: #dfe9d1;
    --salmon: #f07b65;
    --pink: #f6a898;
    --yellow: #efd47f;
    --orange: #f0a34c;
    --blue-light: #a8d2e1;
    --teal: #3f9588;
    --teal-text: #2b8a7c;
    --red-head: #c7432d;
    --ink: #2c2c2c;
    --white: #ffffff;
    --stage: #34373a;
  }
  * { box-sizing: border-box; margin: 0; padding: 0; }
  html, body { width: 1200px; height: 959px; overflow: hidden; }
  body {
    background: var(--stage);
    font-family: "Comic Neue", "Comic Sans MS", cursive;
    position: relative;
  }
  .card {
    position: absolute;
    top: 79px;
    width: 362px;
    height: 830px;
    background: var(--white);
    overflow: hidden;
  }
  .card--front { left: 149px; }
  .card--back { left: 677px; }
  .tile, .photo { position: absolute; }
  .tile--green { background: var(--green); }
  .tile--green-light { background: var(--green-light); }
  .tile--salmon { background: var(--salmon); }
  .tile--pink { background: var(--pink); }
  .tile--yellow { background: var(--yellow); }
  .tile--orange { background: var(--orange); }
  .tile--blue-light { background: var(--blue-light); }
  .tile--teal { background: var(--teal); }

  .tagline {
    position: absolute; left: 164px; top: 12px; width: 180px;
    color: var(--white); font-weight: 700; font-size: 22px; line-height: 38px;
  }
  .catch-phrase {
    position: absolute; left: 14px; top: 160px;
    color: var(--yellow); font-weight: 700; font-size: 47px; line-height: 56px;
  }
  .catch-phrase span { display: block; }
  .catch-phrase span + span { padding-left: 36px; }

  .who {
    position: absolute; left: 153px; top: 460px; width: 204px; color: var(--white);
  }
  .who h2 { font-size: 20px; font-weight: 700; margin-bottom: 14px; }
  .who p { font-size: 13px; line-height: 15.6px; }

  .brand {
    position: absolute; display: flex; align-items: center; gap: 6px;
    color: var(--teal); font-weight: 700; font-size: 17px;
  }
  .brand__dot { width: 12px; height: 12px; border-radius: 50%; background: var(--orange); }
  .card--front .brand { left: 6px; top: 728px; }
  .card--back .brand { left: 0; right: 0; top: 790px; justify-content: center; }

  .front-footer {
    position: absolute; left: 0; top: 779px; width: 362px; height: 51px;
    background: var(--teal); color: var(--white); font-size: 11px;
    text-align: center; padding-top: 16px;
  }

  .recipe-title {
    position: absolute; left: 173px; top: 316px;
    color: var(--red-head); font-weight: 700; font-size: 20px;
  }
  .recipe-intro {
    position: absolute; left: 173px; top: 358px; width: 165px;
    color: var(--teal-text); font-weight: 700; font-size: 11.5px; line-height: 12.5px;
  }
  .recipe {
    position: absolute; left: 34px; top: 409px; width: 300px;
    color: var(--ink); font-size: 8.6px; line-height: 11.4px;
  }
  .recipe h3 { font-size: 10px; font-weight: 700; margin-top: 8px; }
  .recipe h3:first-child { margin-top: 0; }
  .recipe .h-ingredients, .recipe .h-method { color: var(--red-head); }
  .recipe .h-description { color: var(--teal-text); }

  .social {
    position: absolute; left: 0; right: 0; top: 682px;
    text-align: center; color: var(--teal); font-weight: 700; font-size: 16px;
  }

  .contact {
    position: absolute; left: 0; right: 0; top: 738px;
    text-align: center; color: var(--ink); font-weight: 700; font-size: 11.5px; line-height: 14px;
  }
</style>
</head>
<body>

<section class="card card--front" aria-label="Rack card front">
  <div class="photo" role="img" aria-label="Two young girls playing soccer on a grass field" style="left:0;top:0;width:145px;height:134px;background:linear-gradient(180deg,#8fb6dc 0%,#c9dcea 55%,#6f9a45 75%,#5b8236 100%);"></div>
  <div class="tile tile--green" style="left:145px;top:0;width:217px;height:141px;"></div>
  <p class="tagline">Charity Providing Athletic Footwear to Kids!</p>

  <div class="tile tile--salmon" style="left:0;top:150px;width:289px;height:143px;"></div>
  <h1 class="catch-phrase"><span>Cheer Each</span><span>Game</span></h1>
  <div class="photo" role="img" aria-label="Child blowing soap bubbles" style="left:289px;top:150px;width:73px;height:70px;background:linear-gradient(160deg,#6c9c4c,#c58a6a 60%,#b54a3a);"></div>
  <div class="tile tile--blue-light" style="left:289px;top:223px;width:73px;height:70px;"></div>

  <div class="tile tile--yellow" style="left:0;top:298px;width:73px;height:64px;"></div>
  <div class="photo" role="img" aria-label="Girl in ballet outfit lying on the floor" style="left:73px;top:298px;width:72px;height:64px;background:linear-gradient(180deg,#f3eef0,#e7b9c9 70%,#d9c3b5);"></div>
  <div class="tile tile--orange" style="left:145px;top:298px;width:72px;height:64px;"></div>
  <div class="photo" role="img" aria-label="Girl jumping in front of a brick wall" style="left:217px;top:298px;width:72px;height:140px;background:linear-gradient(180deg,#b06a4e,#9b5a42 60%,#7fa7b8 80%,#8d5a44);"></div>
  <div class="tile tile--green-light" style="left:289px;top:298px;width:73px;height:69px;"></div>

  <div class="photo" role="img" aria-label="Young golfer swinging a club" style="left:0;top:371px;width:73px;height:67px;background:linear-gradient(180deg,#cfd9dc,#8fa87a 60%,#6f9446);"></div>
  <div class="tile tile--salmon" style="left:73px;top:371px;width:72px;height:67px;"></div>
  <div class="tile tile--blue-light" style="left:145px;top:371px;width:72px;height:67px;"></div>
  <div class="tile tile--green" style="left:289px;top:371px;width:73px;height:67px;"></div>

  <div class="tile tile--teal" style="left:0;top:443px;width:362px;height:258px;"></div>
  <div class="tile" style="left:0;top:443px;width:145px;height:258px;background:var(--white);"></div>
  <div class="tile tile--blue-light" style="left:0;top:447px;width:71px;height:66px;"></div>
  <div class="tile tile--green-light" style="left:73px;top:447px;width:72px;height:66px;"></div>
  <div class="tile tile--green" style="left:0;top:517px;width:71px;height:71px;"></div>
  <div class="tile tile--teal" style="left:73px;top:517px;width:72px;height:71px;"></div>
  <div class="photo" role="img" aria-label="Boy kicking a soccer ball" style="left:0;top:592px;width:71px;height:70px;background:linear-gradient(180deg,#7aa04f,#5e8a3a 70%,#3d6fa8);"></div>
  <div class="tile tile--yellow" style="left:73px;top:592px;width:72px;height:70px;"></div>
  <div class="tile tile--teal" style="left:0;top:666px;width:145px;height:35px;"></div>

  <div class="who">
    <h2>Who we are:</h2>
    <p>We are a 501(c)3 non-profit organization providing athletic footwear to disadvantaged and at-risk youth. The proper footwear allows participation in sports activities providing a healthy outlet for energy, increased self confidence, reduced juvenile crime rates, decline in alcohol, tobacco and drug dependency, strengthened relationships and enhanced academic performance.</p>
  </div>

  <div class="brand"><span class="brand__dot"></span>Hop-and-Laces</div>
  <div class="photo" role="img" aria-label="Pile of sports balls: soccer, basketball, football, volleyball, tennis and golf" style="left:170px;top:704px;width:192px;height:74px;background:linear-gradient(90deg,#e9e9e9,#d77a3a 35%,#8a4a2a 60%,#f1ece0 85%,#cfe05a);"></div>

  <p class="front-footer">www.hop-and-laces.org</p>
</section>

<section class="card card--back" aria-label="Rack card back">
  <div class="tile tile--blue-light" style="left:0;top:0;width:73px;height:73px;"></div>
  <div class="photo" role="img" aria-label="Children's legs in ice skates on an ice rink" style="left:73px;top:0;width:289px;height:219px;background:linear-gradient(180deg,#c9cfd6,#eef1f4 45%,#d8dde2 100%);"></div>
  <div class="photo" role="img" aria-label="Small child with a soccer ball on grass" style="left:0;top:77px;width:73px;height:68px;background:linear-gradient(180deg,#86ad5b,#5f8a3a);"></div>
  <div class="tile tile--green" style="left:0;top:150px;width:71px;height:69px;"></div>
  <div class="tile tile--green-light" style="left:73px;top:150px;width:72px;height:69px;"></div>

  <div class="photo" role="img" aria-label="Baseball player sliding into base" style="left:0;top:224px;width:145px;height:69px;background:linear-gradient(135deg,#a3784c,#c99a6a 50%,#6d8a3e);"></div>
  <div class="tile tile--yellow" style="left:148px;top:224px;width:70px;height:69px;"></div>
  <div class="tile tile--pink" style="left:221px;top:224px;width:70px;height:69px;"></div>
  <div class="photo" role="img" aria-label="Little girl in a pink ballet outfit sitting on the floor" style="left:292px;top:224px;width:70px;height:69px;background:linear-gradient(180deg,#f4eeea,#e8c0c8 65%,#cfa98a);"></div>

  <div class="tile tile--salmon" style="left:0;top:300px;width:71px;height:68px;"></div>
  <div class="tile tile--orange" style="left:73px;top:300px;width:72px;height:68px;"></div>

  <h2 class="recipe-title">Recipies:</h2>
  <p class="recipe-intro">Lorem ipsum dolor sitte amet lorem sectetuer adipiscing, sed diam erat nibh euismod tincidunt ut laoreet.</p>

  <div class="recipe">
    <h3 class="h-ingredients">INGREDIENTS</h3>
    <p>Lorem ipsum dolor sit amet, consectetuer adipiscing, sed diam nonummy nibh euismod tincidunt ut erat laoreet dolore magna illis aliquam erat volutpat. Ut wisi enim ad erat minim veniam, quis nostrud exerci tation ullamcorper.</p>
    <h3 class="h-description">DESCRIPTION</h3>
    <p>Pusto odio dignissim qui blandit praesent luptatum zzril delenit augue duis dolore te feu gait nulla facilisi. Lorem ipsum dolor sit amet, erat consectetuer adipiscing elit.</p>
    <h3 class="h-method">METHOD TO PREPARE</h3>
    <p>Duis autem vel eum iriure dolor in hendrerit in placerat vulputate velit esse lorem molesti consequat, vel illum dolore eu feugiat nulla facilisis at vero eros et erat accumsan et ius odio te dignissim qui blandit ulluy praesent luptatum zzril oi delenit augue duis dolore.</p>
    <p>Ut wisi enim ad minim veniam, quis nostrud exerci tation ullamcorper. Et iusto odio dig nissim qui blandit praesent luptatum zzril iu delenit augue duis dolore te feugait nulla tera facilisi. Lorem ipsum dolor sit amet, erat consectetuer adipiscing elit.</p>
    <p>Odio dignissim qui blandit praesent luptatum zzril delenit augue duis dolore te feugait nulla facilisi. Nam liber tempor cum soluta nobis eleifend option congue nihil imperdiet doming id quod mazim placerat facer wisi enim ad minim veniam possim assum.</p>
  </div>

  <div class="photo" role="img" aria-label="Soccer ball on grass at sunset" style="left:0;top:686px;width:70px;height:69px;background:linear-gradient(180deg,#e8a04a,#f3d08a 45%,#5f8a3a);"></div>
  <div class="tile tile--green" style="left:0;top:758px;width:70px;height:72px;"></div>

  <p class="social">Find us on chatterbook</p>

  <p class="contact">PO Box 57392, Phoenix, AZ 85077;<br>www.hop-and-laces.org</p>

  <div class="brand"><span class="brand__dot"></span>Hop-and-Laces</div>
</section>

</body>
</html>
```